Business Card Design Project

We need a double-sided business card design for our e-commerce company. Be as creative as you can.

Reason: Change of logo

Target Market(s)

Business owners

Industry/Entity Type

E-Commerce

Requirements
Must have
• Name (editable)
Mobile number -editable
www.trizvo.com - MUST STAND OUT ALONE
Office address:
27 Pellow Road
#09-04 Corbell Tower
Singapore 058214

```html
<!DOCTYPE html>
<html lang="en">
<head>
<meta charset="utf-8">
<title>Trizvo Business Card</title>
<link rel="stylesheet" href="https://fonts.googleapis.com/css2?family=Cinzel:wght@400;600&family=Questrial&display=swap">
<style>
  :root {
    --bg: #dcdcdc;
    --ink-dark: #1b1f1f;
    --paper: #f9f7fa;
    --green: #2e6b2a;
    --green-bright: #4aa33a;
    --green-lime: #7ac143;
    --text: #1a1a1a;
    --muted: #8a8a8a;
  }
  * { box-sizing: border-box; margin: 0; padding: 0; }
  html, body { width: 1200px; height: 985px; overflow: hidden; }
  body {
    background: var(--bg);
    position: relative;
    font-family: "Questrial", sans-serif;
  }
  .card {
    position: absolute;
    left: 250px;
    width: 700px;
    height: 400px;
    border-radius: 28px;
    overflow: hidden;
    box-shadow: 0 10px 24px rgba(0,0,0,0.18);
  }
  .brand-name {
    font-family: "Questrial", sans-serif;
    color: var(--green-bright);
    font-size: 64px;
    letter-spacing: 4px;
    line-height: 1;
  }
  .tagline {
    font-family: "Questrial", sans-serif;
    font-size: 15px;
    letter-spacing: 6px;
    text-transform: uppercase;
    margin-top: 10px;
    white-space: nowrap;
  }

  /* Back side */
  .card--back { top: 50px; background: var(--ink-dark); }
  .card--back .brand {
    position: absolute; top: 120px; left: 0; width: 100%;
    text-align: center;
  }
  .card--back .tagline { color: #ffffff; }
  .card--back .web {
    position: absolute; top: 285px; width: 100%; text-align: center;
    color: var(--green-lime); font-size: 17px; letter-spacing: 6px;
  }

  /* Front side */
  .card--front { top: 530px; background: var(--paper); }
  .card--front .waves { position: absolute; inset: 0; }
  .card--front .brand { position: absolute; top: 100px; left: 140px; }
  .card--front .brand-name { font-size: 56px; }
  .card--front .tagline { color: var(--muted); font-size: 13px; margin-top: 6px; }
  .person {
    position: absolute; left: 56px; top: 208px;
    color: var(--text); font-family: "Cinzel", serif;
  }
  .person-name { font-size: 23px; letter-spacing: 1px; }
  .person-title { font-size: 12px; margin-top: 4px; letter-spacing: 1px; }
  .contact {
    position: absolute; left: 370px; top: 262px;
    font-family: "Cinzel", serif; font-style: normal; font-size: 16px; color: var(--text);
    line-height: 1.3; letter-spacing: 0.5px;
  }
  .contact-row { display: flex; align-items: center; gap: 8px; margin-top: 4px; }
  .contact-row svg { width: 16px; height: 16px; flex: none; }
</style>
</head>
<body>

<section class="card card--back" aria-label="Card back">
  <div class="brand">
    <div class="brand-name">Trizvo</div>
    <div class="tagline">Every Cart Counts!</div>
  </div>
  <div class="web">www.TRIZVO.com</div>
</section>

<section class="card card--front" aria-label="Card front">
  <svg class="waves" viewBox="0 0 700 400" preserveAspectRatio="none" aria-hidden="true">
    <path d="M0,0 H700 V300 C600,270 520,120 400,60 C300,20 150,25 0,70 Z" fill="var(--ink-dark)"/>
    <path d="M60,110 C170,40 330,20 470,75 C340,40 190,55 60,110 Z" fill="var(--green)"/>
    <path d="M520,175 C570,230 620,262 700,275 L700,288 C610,278 560,240 520,175 Z" fill="var(--green)"/>
  </svg>
  <div class="brand">
    <div class="brand-name">Trizvo</div>
    <div class="tagline">Every Cart Counts!</div>
  </div>
  <div class="person">
    <div class="person-name">Name (Editable)</div>
    <div class="person-title">Your Titel</div>
  </div>
  <address class="contact">
    <div>27 Pellow Road</div>
    <div>#09-04 Corbell Tower</div>
    <div>Singapore 058214</div>
    <div class="contact-row">
      <svg viewBox="0 0 16 16" aria-hidden="true"><rect x="1" y="3" width="14" height="11" rx="2" fill="var(--green)"/><rect x="5" y="6" width="6" height="5" rx="1" fill="var(--paper)"/></svg>
      <span>0000 0000</span>
    </div>
    <div class="contact-row">
      <svg viewBox="0 0 16 16" aria-hidden="true"><circle cx="8" cy="8" r="7" fill="none" stroke="var(--green)" stroke-width="1.5"/><ellipse cx="8" cy="8" rx="3" ry="7" fill="none" stroke="var(--green)" stroke-width="1.2"/><line x1="1" y1="8" x2="15" y2="8" stroke="var(--green)" stroke-width="1.2"/></svg>
      <span>www.trizvo.com</span>
    </div>
  </address>
</section>

</body>
</html>
```